Skyrest Aero Works Logo

I need a website and logo for the parent company Skyrest Aero Works, which encompasses general aviation aircraft repair, small aircrat rental and flight school. The company is based in Halvern Springs, Calder at the Hollins Field airport. A saying that can be incorporated somehere could be, "Quality flying is safe flying", "Safety in mind is no accident" ,. I need a website and logo.

The company started as a repair shop performing repairs and inspections on Darrow, Keller, Varnell and Talbot general aviation aircraft, all models of single engine piston, multi engine piston, and single engine turboprop with an emphasis on Darrow Solace and AeroKin turbo prop aircraft. We have se=ince entered the aircraft rental and flight instruction market using the Varnell 318 ang Darrow Pilgrim aircraft.

Number of Pages; I don't know. Maybe 5 ? A home page for Skyrest Aero Works, page for maintenance and repairs and a couple for the rental and school. The maintenance shop is busy, always has been. I need to get the rental and school advertised and busy.

I have a logo for the maintenance shop shirts, not for the school. I do not have the file. I paid a business locally to do that and print on the shirts. They have the file.

Target Market(s)

In our flight school rental fleet department, we are looking for persons wishing to obtain their private pilot license and continuing on into their commercial and instrument ratings. In the aircraft maintenance department, we are looking for new customers who want a better and more quality relationship with their aircraft maintenance provider who will give more detail and quality in the repairs with an emphasis on safety and fewer problems between scheduled maintenance cycles on their aircraft. Skyrest's owner, Dale Fenwick, has been performing aircraft maintenance in the Atlanta area for 27 years. He has built a steady customer base through those years.

```html
<!DOCTYPE html>
<html lang="en">
<head>
<meta charset="utf-8">
<title>Skyrest Aero Works</title>
<link rel="stylesheet" href="https://fonts.googleapis.com/css2?family=Oswald:wght@400;500&family=Mulish:wght@400;600;700&display=swap">
<style>
:root{
  --blue:#1a44a8;
  --blue-dark:#12338a;
  --ink:#1b1b1b;
  --text:#444;
  --white:#fff;
  --black:#000;
  --photo-dark:#3b3e44;
  --photo-mid:#6b7078;
}
*{box-sizing:border-box;margin:0;padding:0}
html,body{width:1200px;height:4655px;overflow:hidden}
body{position:relative;background:var(--white);font-family:'Mulish',sans-serif;color:var(--text)}
.abs{position:absolute}
.heading{font-family:'Oswald',sans-serif;font-weight:400;color:var(--ink);text-transform:uppercase;letter-spacing:-.5px}
.rule{width:48px;height:3px;background:var(--ink)}
.btn{position:absolute;display:flex;align-items:center;justify-content:center;background:var(--blue);color:var(--white);font-family:'Mulish',sans-serif;font-weight:600;font-size:15px;letter-spacing:.5px;border-radius:12px 0 12px 0;height:44px;width:140px}
.copy p{font-size:12.6px;line-height:22px;color:var(--text);margin-bottom:10px}

/* top bar */
.topbar{left:0;top:0;width:1200px;height:45px;background:var(--blue);color:var(--white)}
.social{left:163px;top:14px;display:flex;gap:12px}
.social span{width:14px;height:14px;border-radius:50%;background:var(--white)}
.call{right:160px;top:12px;display:flex;align-items:center;gap:8px;font-size:13.5px}
.call b{font-weight:700}

/* hero */
.hero{left:0;top:45px;width:1200px;height:655px;background:linear-gradient(110deg,#2a2c31 0%,var(--photo-dark) 45%,var(--photo-mid) 70%,#9a9ea6 100%)}
.brand{left:163px;top:58px;color:var(--white)}
.brand .name{font-family:'Oswald',sans-serif;font-weight:500;font-size:30px;line-height:34px;text-transform:uppercase}
.nav{left:508px;top:74px;display:flex;gap:28px;font-family:'Oswald',sans-serif;font-size:13px;color:var(--white);text-transform:uppercase}
.hero-title{left:163px;top:240px;font-family:'Oswald',sans-serif;font-weight:400;font-size:54px;line-height:64px;color:var(--white)}

/* about */
.about-head{left:163px;top:815px;font-family:'Oswald',sans-serif}
.about-head .sm{font-size:24px;color:var(--blue);font-family:'Mulish',sans-serif}
.about-head .lg{font-size:42px;color:var(--black);line-height:48px;font-weight:500;text-transform:uppercase}
.about-head .line{width:56px;height:3px;background:var(--blue);margin-top:8px}
.about-copy{left:442px;top:778px;width:582px}

/* services */
.svc-title{left:0;width:1200px;top:1205px;text-align:center;font-size:38px}
.card{position:absolute;width:422px;height:245px;border-radius:10px;display:flex;align-items:center;justify-content:center;font-family:'Oswald',sans-serif;font-size:27px;color:var(--white);text-transform:uppercase}

/* sky */
.sky-title{left:0;width:1200px;top:2362px;text-align:center;font-size:36px;text-transform:none}
.sky-text{left:200px;width:800px;top:2420px;text-align:center;font-size:15px;line-height:27px;color:#2a3a6a}

/* features */
.feat-title{font-size:36px}

/* reviews */
.review-card{left:230px;top:3770px;width:752px;height:290px;background:var(--white);border-radius:60px 0 60px 0;box-shadow:0 8px 30px rgba(0,0,0,.13)}
.quote-text{left:313px;top:3862px;width:635px;font-size:12px;line-height:19.5px;letter-spacing:.6px;color:#333}
.dots{left:1034px;top:3866px;display:flex;flex-direction:column;gap:14px}
.dots span{width:10px;height:10px;border-radius:50%;background:#c9ccd2}
.dots span.on{background:var(--blue);box-shadow:0 0 0 2px #fff,0 0 0 3px var(--blue)}

/* footer */
.foot-h{font-family:'Oswald',sans-serif;font-size:19px;color:var(--white);text-transform:uppercase}
.links{left:163px;top:4352px;list-style:none}
.links li{color:var(--white);font-size:13.5px;line-height:35.5px}
.links li::before{content:"›";margin-right:14px}
.contact{left:465px;top:4350px}
.citem{display:flex;gap:18px;margin-bottom:20px;color:var(--white)}
.ic{width:28px;height:28px;border-radius:50%;background:var(--blue);flex:none;display:flex;align-items:center;justify-content:center}
.citem b{display:block;font-size:14px;font-weight:600}
.citem span{font-size:13px;line-height:22px}
.foot-brand{left:830px;top:4440px;color:var(--white);text-align:center;width:212px}
.foot-brand .name{font-family:'Oswald',sans-serif;font-weight:500;font-size:30px;line-height:36px;text-transform:uppercase}
.copyright{left:0;width:1200px;top:4617px;text-align:center;color:var(--white);font-size:13.5px}
</style>
</head>
<body>

<div class="abs topbar">
  <div class="abs social" aria-label="Social links"><span></span><span></span><span></span><span></span></div>
  <div class="abs call">
    <svg width="22" height="22" viewBox="0 0 22 22"><circle cx="11" cy="11" r="11" fill="#fff"/><path d="M7 6c1-1 2 0 2.5 1.5s-.5 2 0 3 2 2.5 3 3 1.5-1 3 0S17 16 16 17c-3 1-10-6-9-11z" fill="#1a44a8"/></svg>
    <span><b>Call Us</b> 123-456-7890</span>
  </div>
</div>

<div class="abs hero" role="img" aria-label="Aircraft maintenance hangar with a white single-engine plane and a mechanic at work"></div>
<svg class="abs" style="left:0;top:540px" width="1200" height="170" viewBox="0 0 1200 170">
  <polygon points="0,20 928,160 1200,20 1200,170 0,170" fill="#fff"/>
  <polygon points="0,15 928,155 1200,18 1200,30 928,162 0,28" fill="#1a44a8"/>
  <polygon points="0,24 928,162 1200,26 1200,36 928,170 0,36" fill="#fff"/>
</svg>
<div class="abs brand"><div class="name">Skyrest Aero Works</div></div>
<nav class="abs nav"><span>Home</span><span>Maintenance &amp; Repairs</span><span>Aircraft Rental</span><span>Flight School</span><span>Contact Us</span></nav>
<h1 class="abs hero-title">"Quality Flying Is Safe<br>Flying"</h1>
<div class="btn" style="left:163px;top:393px;width:140px">CONTACT US</div>

<div class="abs about-head">
  <div class="sm">ABOUT</div>
  <div class="lg">Skyrest</div>
  <div class="sm" style="font-size:20px">Aero Works</div>
  <div class="line"></div>
</div>
<div class="abs about-copy copy">
  <p>Lorem ipsum dolor sit amet, consectetur adipiscing elit, sed do eiusmod tempor incididunt ut labore et dolore magna aliqua. Ut enim ad minim veniam, quis nostrud exercitation ullamco laboris nisi ut aliquip ex ea commodo consequat. Duis aute irure dolor in reprehenderit in voluptate velit esse cillum dolore eu fugiat nulla pariatur</p>
  <p>Lorem ipsum dolor sit amet, consectetur adipiscing elit, sed do eiusmod tempor incididunt ut labore et dolore magna aliqua. Ut enim ad minim veniam</p>
</div>

<svg class="abs" style="left:0;top:1020px" width="1200" height="682" viewBox="0 0 1200 682" role="img" aria-label="Faded photo of a light aircraft on an airfield">
  <defs><linearGradient id="svcbg" x1="0" y1="0" x2="0" y2="1"><stop offset="0" stop-color="#e9ebee"/><stop offset=".5" stop-color="#d9dcdf"/><stop offset="1" stop-color="#d3d8cf"/></linearGradient></defs>
  <polygon points="0,120 270,0 1200,125 1200,682 0,682" fill="url(#svcbg)"/>
</svg>
<h2 class="abs heading svc-title">What We Do</h2>
<div class="abs rule" style="left:576px;top:1268px"></div>
<div class="card" style="left:163px;top:1312px;background:linear-gradient(135deg,#4a4d52,#2d2f33)" role="img" aria-label="Plane in the hangar for maintenance">Maintenance</div>
<div class="card" style="left:617px;top:1312px;background:linear-gradient(135deg,#3d4048,#5a5d63)" role="img" aria-label="Engine repair in the hangar">Repairs</div>
<div class="card" style="left:163px;top:1587px;background:linear-gradient(135deg,#3f62b8,#7f95c4)" role="img" aria-label="Training aircraft cockpit">Flight School</div>
<div class="card" style="left:617px;top:1587px;background:linear-gradient(180deg,#4b4a3c,#3a3a33)" role="img" aria-label="Rental aircraft on the runway">Aircraft Rental</div>
<div class="btn" style="left:530px;top:1868px">CONTACT US</div>

<svg class="abs" style="left:0;top:2040px" width="1200" height="650" viewBox="0 0 1200 650" role="img" aria-label="Blue sky with a small plane in flight above the clouds">
  <defs><linearGradient id="sky" x1="0" y1="0" x2="0" y2="1"><stop offset="0" stop-color="#1a44a8"/><stop offset=".35" stop-color="#3e6cc4"/><stop offset=".6" stop-color="#8fb0e2"/><stop offset=".85" stop-color="#e4ecf7"/><stop offset="1" stop-color="#f4f7fb"/></linearGradient></defs>
  <path d="M0,60 Q600,-10 1200,60 L1200,600 Q1150,580 1100,605 Q1050,585 1000,605 Q950,585 900,605 Q850,585 800,605 Q750,585 700,605 Q650,585 600,605 Q550,585 500,605 Q450,585 400,605 Q350,585 300,605 Q250,585 200,605 Q150,585 100,605 Q50,585 0,605 Z" fill="url(#sky)"/>
</svg>
<h2 class="abs heading sky-title">Lorem Ipsum Dolor Sit Amet Conse Ctetur</h2>
<p class="abs sky-text">At vero eos et accusamus et iusto odio dignissimos ducimus qui blanditiis praesentium voluptatum deleniti atque corrupti quos dolores et quas molestias excepturi sint.</p>
<div class="btn" style="left:530px;top:2491px">CONTACT US</div>

<h2 class="abs heading feat-title" style="left:163px;top:2800px">Aircraft Rental</h2>
<div class="abs rule" style="left:163px;top:2862px"></div>
<div class="abs copy" style="left:163px;top:2897px;width:440px">
  <p>Lorem ipsum dolor sit amet, consectetur adipiscing elit, sed do lorem eiusmod tempor incididunt ut labore et dolore magna aliqua. Ut enim ad minim veniam, quis</p>
  <p>Lorem ipsum dolor sit amet, consectetur adipiscing elit, sed do lorem eiusmod tempor incididunt ut labore et dolore magna aliqua. Ut enim ad minim veniam, quis</p>
</div>
<div class="btn" style="left:163px;top:3052px">CONTACT US</div>
<svg class="abs" style="left:758px;top:2808px" width="282" height="284" viewBox="0 0 282 284"><polygon points="268,0 282,0 282,284 0,284 20,270 268,270" fill="#1a44a8"/></svg>
<div class="abs" style="left:708px;top:2758px;width:318px;height:318px;background:linear-gradient(180deg,#a9b8c9 0%,#8fa18a 45%,#3c3f44 60%,#2c2e33 100%)" role="img" aria-label="White and blue rental plane parked on the apron"></div>

<svg class="abs" style="left:163px;top:3238px" width="282" height="280" viewBox="0 0 282 280"><polygon points="0,0 14,14 14,266 262,266 282,280 0,280" fill="#1a44a8"/></svg>
<div class="abs" style="left:176px;top:3185px;width:319px;height:318px;background:linear-gradient(180deg,#a8bbd2 0%,#c9d4df 38%,#7f9a4e 60%,#5f7d33 100%)" role="img" aria-label="Red and white training plane on a grass airfield"></div>
<h2 class="abs heading feat-title" style="left:601px;top:3225px">Flight School</h2>
<div class="abs rule" style="left:601px;top:3287px"></div>
<div class="abs copy" style="left:601px;top:3322px;width:440px">
  <p>Lorem ipsum dolor sit amet, consectetur adipiscing elit, sed do lorem eiusmod tempor incididunt ut labore et dolore magna aliqua. Ut enim ad minim veniam, quis</p>
  <p>Lorem ipsum dolor sit amet, consectetur adipiscing elit, sed do lorem eiusmod tempor incididunt ut labore et dolore magna aliqua. Ut enim ad minim veniam, quis</p>
</div>
<div class="btn" style="left:596px;top:3480px">CONTACT US</div>

<h2 class="abs heading" style="left:0;width:1200px;top:3660px;text-align:center;font-size:36px">Customer Reviews</h2>
<div class="abs rule" style="left:576px;top:3722px"></div>
<div class="abs review-card"></div>
<div class="abs" style="left:177px;top:3808px;width:403px;height:3px;background:var(--blue)"></div>
<svg class="abs" style="left:872px;top:3784px" width="62" height="44" viewBox="0 0 62 44"><path d="M0,44V24Q0,4 22,0V10Q12,12 12,20H26V44ZM34,44V24Q34,4 56,0V10Q46,12 46,20H60V44Z" fill="#7f93c9"/></svg>
<div class="abs" style="left:180px;top:3862px;width:97px;height:97px;border:3px solid var(--blue);padding:5px"><div style="width:100%;height:100%;background:linear-gradient(180deg,#dfe3e8,#b9c2cc)" role="img" aria-label="Customer portrait"></div></div>
<p class="abs quote-text">" Lorem ipsum dolor sit amet, consectetur adipiscing elit, sed diam nonummy nibh euismod tincidunt ut laoreet dolore magna aliquam erat volutpat. Ut wisi enim ad minim veniam, quis nostrud exerci tation ullamcorper suscipit lobortis nisl ut aliquip ex ea commodo consequat.Lorem ipsum dolor sit amet, consectetur adipiscing elit, sed diam nonummy nibh euismod tincidunt ut laoreet dolore magna aliquam erat volutpat. Ut wisi enim ad minim veniam"</p>
<div class="abs" style="left:654px;top:4011px;font-size:12px;font-weight:700;color:#222">Corin Ashby</div>
<div class="abs" style="left:758px;top:4018px;width:248px;height:3px;background:var(--blue)"></div>
<div class="abs dots"><span class="on"></span><span></span><span></span><span></span></div>

<svg class="abs" style="left:0;top:4155px" width="1200" height="500" viewBox="0 0 1200 500">
  <polygon points="0,130 270,0 1200,140 1200,500 0,500" fill="#1a44a8"/>
  <polygon points="0,145 270,15 1200,150 1200,500 0,500" fill="#000"/>
</svg>
<div class="abs foot-h" style="left:163px;top:4302px">Quick Links</div>
<ul class="abs links">
  <li>Home</li><li>Services</li><li>Maintenance &amp; Repairs</li><li>Aircraft Rental</li><li>Flight School</li><li>Contact Us</li>
</ul>
<div class="abs foot-h" style="left:465px;top:4302px">Contact Details</div>
<div class="abs contact">
  <div class="citem"><div class="ic"><svg width="12" height="16" viewBox="0 0 12 16"><path d="M6,0A6,6 0 0 1 12,6C12,10 6,16 6,16S0,10 0,6A6,6 0 0 1 6,0Z" fill="#fff"/><circle cx="6" cy="6" r="2.2" fill="#1a44a8"/></svg></div><div><b>Address</b><span>12 Lorem Imsum, Street Name,<br>Halvern Springs, Calder</span></div></div>
  <div class="citem"><div class="ic"><svg width="14" height="14" viewBox="0 0 14 14"><path d="M2,1c1.5-1 2.5 0 3 2s-1 2 0 3.5 2.5 3 3.5 3 2-1.5 4 0-.5 4-2 4C6,13 1,8 2,1z" fill="#fff"/></svg></div><div><b>Phone</b><span>123.456.7890</span></div></div>
  <div class="citem"><div class="ic"><svg width="14" height="10" viewBox="0 0 14 10"><rect width="14" height="10" rx="1" fill="#fff"/><path d="M0,0L7,6L14,0" stroke="#1a44a8" stroke-width="1.4" fill="none"/></svg></div><div><b>Email</b><span>inquiry@skyrestaero.com</span></div></div>
</div>
<div class="abs foot-brand"><div class="name">Skyrest<br>Aero Works</div></div>
<div class="abs" style="left:163px;top:4588px;width:875px;height:1px;background:#333"></div>
<div class="abs copyright">© 2023 Skyrest Aero Works. All Rights Reserved.</div>

</body>
</html>
```